10' x 4' outdoor vinyl banner

My company prepare and sell delicious Maryland Style Gourmet Crab Cake sandwiches at public events like fairs, festivals and concerts.
We use a 10' x 10' tent to prepare and sell this sandwiches at those events. I need a 10x4 (10 feet long by 4 feet high) banner display for the top of the tent. The same design should be scalable to another 10x3 banner for the bottom of the tent.
I need a general design of a banner with a wording that should be very attention catching
The wording is: "Maryland Crab Cake Sandwiches"
I would like also to incorporate into the design a blue crab (this is the name of specific type of crab that I'm looking for, is not just a crab painted in blue)
The theme of the design should be the sea, the shoreline, maybe some fishing boat, waves, etc, in that spirit.
I would like to use a nice blue color in the background, as we are talking about the sea and marine themes.
There are some other wordings that I would like to incorporate into the banner:
A Traditional Chesapeake Bay recipe with 100% All Natural, Blue Crab Meat . . . Rich and Flavorful . . .
This type should be in smaller size, but still visible, maybe in italics or an elegant font type.
I want something simple, inviting, like my delicious sandwiches.

```html
<!DOCTYPE html>
<html lang="en">
<head>
<meta charset="UTF-8">
<title>Maryland Crab Cake Sandwiches – Tent Banner</title>
<link rel="stylesheet" href="https://fonts.googleapis.com/css2?family=Uncial+Antiqua&family=Comic+Neue:wght@700&display=swap">
<style>
  :root {
    --sea-deep: #0b3fa8;
    --sea-mid: #1d8fd4;
    --sea-shallow: #3fc6d9;
    --surf: #d8f1f2;
    --sand-wet: #d9b987;
    --sand-dry: #e8c896;
    --title-dark: #8a0c10;
    --title-red: #d41a1c;
    --glow: #ffffff;
    --ink: #1c1c1c;
    --crust: #b0662a;
    --crust-dark: #6e3615;
  }
  html, body {
    margin: 0;
    padding: 0;
    width: 1200px;
    height: 480px;
    overflow: hidden;
    background: #ffffff;
  }
  .banner {
    position: relative;
    width: 1200px;
    height: 480px;
    overflow: hidden;
  }
  .shore-scene {
    position: absolute;
    inset: 0;
    background: linear-gradient(180deg,
      var(--sea-deep) 0%,
      var(--sea-mid) 18%,
      var(--sea-shallow) 45%,
      var(--surf) 66%,
      var(--sand-wet) 76%,
      var(--sand-dry) 100%);
  }
  .sandwich-photo {
    position: absolute;
    left: 537px;
    top: 72px;
    width: 126px;
    height: 100px;
    border-radius: 50% 50% 45% 45%;
    background: radial-gradient(ellipse at 50% 35%, #e0a35a 0%, var(--crust) 55%, var(--crust-dark) 100%);
    box-shadow: 0 0 18px rgba(255,255,255,0.7);
  }
  .headline {
    position: absolute;
    left: 0;
    right: 0;
    margin: 0;
    text-align: center;
    font-family: "Uncial Antiqua", serif;
    font-weight: 400;
    line-height: 1;
  }
  .headline-state {
    top: 180px;
    font-size: 84px;
    color: var(--title-dark);
    text-shadow: 0 0 6px var(--glow), 0 0 12px var(--glow), 2px 3px 2px rgba(0,0,0,0.35);
  }
  .headline-product {
    top: 262px;
    font-size: 62px;
    color: var(--title-red);
    text-shadow: 0 0 6px var(--glow), 0 0 12px var(--glow), 2px 3px 2px rgba(0,0,0,0.35);
  }
  .tagline {
    position: absolute;
    left: 0;
    right: 0;
    top: 352px;
    margin: 0;
    text-align: center;
    font-family: "Comic Neue", cursive;
    font-weight: 700;
    font-size: 25px;
    line-height: 32px;
    color: var(--ink);
    text-shadow: 0 0 4px var(--glow), 0 0 8px var(--glow), 0 0 10px var(--glow);
  }
</style>
</head>
<body>
  <main class="banner">
    <div class="shore-scene" role="img" aria-label="Photograph of turquoise sea waves breaking onto a sandy beach"></div>
    <div class="sandwich-photo" role="img" aria-label="Photograph of a fried soft-shell blue crab sandwich on a bun with lettuce and tomato"></div>
    <h1 class="headline headline-state">Maryland</h1>
    <h2 class="headline headline-product">Crab Cake Sandwiches</h2>
    <p class="tagline">A Traditional Chesapeake Bay recipe with 100% All Natural<br>Blue Crab Meat . . . Rich and Flavorful . . .</p>
  </main>
</body>
</html>
```